Distribution/Printing company needs a web site to inform prospective customers on what we do.

Distribution/Printing/Packaging company needs a web site to inform prospective customers on what we do. Please look at our direct to consumer web site (under development) for an idea of the product lines we sell: storedev.kelbrynwares.com
Logo files are attached as is a flyer that is under development which contains other information about the company (this is to be used for content- not to be posted as is). The web site should be focused on our business customer base and is not intended to be direct to consumer. Site should have a link to our consumer web site.
Site design should be mobile friendly, or mobile could be redirected to a mobile version. This web site will be strictly informational and will not be designed for any sales transactions.

Manufacturing and retail businesses, any other multi-site business that would benefit from centralized pricing and budget controls we can provide (banks, medical/dental offices, educational facilities, etc).

• 1) Top level menu: Products, about us, locations, contact us, news
• 2) page with news/promotions that is easily updated
• 3) "contact us" form (name, company, phone, email address) email link
• 4) link to www.store.kelbrynwares.com with information that lower pricing is available for businesses
• 5) SEO keywords
• 6) Link to powerpoint presentation file
• 1) our phone number should appear on every page near the top

```html
<!DOCTYPE html>
<html lang="en">
<head>
<meta charset="utf-8">
<title>Kelbryn Wares</title>
<link href="https://fonts.googleapis.com/css2?family=Open+Sans:wght@400;600;700&display=swap" rel="stylesheet">
<style>
:root{
  --dark:#2b2b2b;
  --darker:#1e1e1e;
  --panel:#262626;
  --text:#555;
  --muted:#8a8a8a;
  --light:#efefef;
  --white:#fff;
  --line:#dcdcdc;
}
*{margin:0;padding:0;box-sizing:border-box}
html,body{width:729px;height:1200px;overflow:hidden}
body{font-family:'Open Sans',sans-serif;background:var(--white);color:var(--text);position:relative}
.abs{position:absolute}
.header{left:0;top:0;width:729px;height:90px;background:var(--dark)}
.brand-mark{left:97px;top:12px;width:26px;height:26px;border:2px solid var(--white);border-radius:50%}
.brand{left:60px;top:47px;color:var(--white);font-weight:700;font-size:12px;letter-spacing:.3px;white-space:nowrap}
.tagline{left:66px;top:65px;color:var(--white);font-size:8px;font-weight:600;white-space:nowrap}
.search{left:440px;top:15px;width:140px;height:23px;border-radius:12px;background:#1c1c1c;color:#999;font-size:6.5px;padding:7px 11px}
.search-btn{left:557px;top:15px;width:23px;height:23px;border-radius:50%;background:var(--white)}
.phone{left:590px;top:15px;width:78px;height:23px;border-radius:12px;background:#1c1c1c;color:#ddd;font-size:6.5px;padding:7px 0 7px 9px;white-space:nowrap}
.phone-btn{left:645px;top:15px;width:23px;height:23px;border-radius:50%;background:var(--white)}
.nav{left:336px;top:55px;height:35px;display:flex}
.nav a{color:#aaa;font-size:7.5px;text-decoration:none;padding:0 11px;line-height:35px;white-space:nowrap}
.nav a.active{background:var(--darker);color:var(--white)}
.hero{left:0;top:92px;width:729px;height:307px;background:linear-gradient(100deg,#d6dadd 0%,#c9cdd0 35%,#b9a68a 60%,#e3ddd2 100%)}
.hero-arrow{top:235px;width:16px;height:20px;background:rgba(80,80,80,.6)}
.caption{left:59px;top:265px;width:187px;height:80px;background:rgba(255,255,255,.85);padding:8px 10px}
.caption h2{font-size:15px;font-weight:400;color:#222;white-space:nowrap}
.caption p{font-size:6.5px;color:#333;margin-top:3px}
.btn-dark{display:inline-block;margin-top:8px;background:#222;color:var(--white);font-size:6.5px;padding:5px 8px;border-radius:2px}
.welcome-img{left:60px;top:433px;width:209px;height:128px;background:linear-gradient(135deg,#b8c4cc,#c8563d 45%,#6aa34b 70%,#c9a77d)}
.welcome{left:282px;top:430px;width:386px}
.welcome h1{font-size:15px;font-weight:700;color:#222;white-space:nowrap}
.welcome p{font-size:6.4px;line-height:11.5px;color:#666;margin-top:6px}
.btn-outline{display:inline-block;margin-top:13px;border:1px solid #aaa;font-size:6.5px;padding:7px 10px;color:#555}
.services{left:59px;top:597px;width:609px;height:200px;background:var(--panel)}
.service{position:absolute;top:13px;width:187px}
.service .img{height:94px}
.service h3{color:var(--white);font-size:13.5px;font-weight:700;margin-top:12px;letter-spacing:.3px}
.service p{color:#888;font-size:6.3px;line-height:10.5px;margin-top:6px}
.service b{display:block;color:var(--white);font-size:6.5px;margin-top:8px}
.products-title{left:60px;top:834px;font-size:10px;font-weight:700;color:#222}
.next{left:659px;top:837px;width:9px;height:9px;border-radius:50%;background:#bbb}
.card{top:856px;width:94px;height:127px;border:1px solid var(--line);text-align:center}
.card .img{margin:3px;height:83px}
.card p{font-size:6.5px;color:#444;margin-top:11px}
.card svg{margin-top:4px}
.footer{left:0;top:1022px;width:729px;height:123px;background:var(--light)}
.col h4{font-size:9.5px;font-weight:400;color:#222}
.col p,.col li{font-size:6.4px;color:#555;line-height:16.5px}
.col .about{line-height:10.5px;margin-top:6px}
.divider{top:1040px;width:1px;height:84px;background:#d4d4d4}
.links{list-style:none;display:grid;grid-template-columns:80px 80px;margin-top:4px}
.links li::before{content:"• "}
.social{display:flex;gap:5px;margin-top:8px}
.social span{width:16px;height:16px;border-radius:50%}
.bottom{left:0;top:1145px;width:729px;height:55px;background:var(--dark);color:#999;font-size:6px}
.round{width:17px;height:17px;border-radius:50%;border:1.5px solid #bbb}
</style>
</head>
<body>
<header class="abs header">
  <div class="abs brand-mark"></div>
  <div class="abs brand">KELBRYN WARES</div>
  <div class="abs tagline">Packaging • Printing • Distribution</div>
  <div class="abs search">Search</div>
  <div class="abs search-btn"><svg width="23" height="23"><circle cx="11" cy="11" r="3.2" fill="none" stroke="#222" stroke-width="1.4"/><line x1="13.3" y1="13.3" x2="15.5" y2="15.5" stroke="#222" stroke-width="1.4"/></svg></div>
  <div class="abs phone">555 201 4480</div>
  <div class="abs phone-btn"><svg width="23" height="23"><path d="M8.5 8c0 4 2.5 6.5 6.5 6.5l.8-1.6-1.8-1-0.9.9c-1-.4-2.5-1.9-2.9-2.9l.9-.9-1-1.8z" fill="#222"/></svg></div>
  <nav class="abs nav"><a class="active">Home</a><a>Products</a><a>About us</a><a>Locations</a><a>News</a><a>Contact us</a></nav>
</header>

<section class="abs hero" role="img" aria-label="Warehouse interior with tall racks of wrapped boxes on pallets"></section>
<div class="abs hero-arrow" style="left:0"><svg width="16" height="20"><path d="M10 5l-4 5 4 5" fill="none" stroke="#ddd"/></svg></div>
<div class="abs hero-arrow" style="left:713px;background:none"><svg width="16" height="20"><path d="M6 5l4 5-4 5" fill="none" stroke="#eee"/></svg></div>
<div class="abs caption">
  <h2>Aliquam erat volutpat</h2>
  <p>Quisque aliquet ex nec est vestibulum pulvinar</p>
  <span class="btn-dark">Read more</span>
</div>

<div class="abs welcome-img" role="img" aria-label="Box filled with office supplies, folders and stapler"></div>
<section class="abs welcome">
  <h1>WELCOME TO KELBRYN WARES</h1>
  <p>Aenean sed quam non sapien faucibus consequat vitae sit amet orci. Praesent quis risus mi. In mollis nulla in pulvinar dictum. Vivamus interdum sagittis felis, ut dapibus ligula feugiat ac. In dictum sapien eu tellus finibus fermentum. Aenean faucibus lacus ut mollis commodo. Donec vestibulum odio sem, ac laoreet massa ullamcorper id. Donec molestie nisi et tellus hendrerit vehicula. Nunc eu ligula sed quam pulvinar maximus in vitae eros. Proin porta fermentum ipsum, vel porttitor turpis venenatis luctus. Vivamus volutpat eu sapien quis tempus. Aenean feugiat viverra lorem ac sagittis. Donec sit amet lectus nec mi tempor laoreet ac nec nunc.</p>
  <span class="btn-outline">READ MORE</span>
</section>

<section class="abs services">
  <div class="service" style="left:11px">
    <div class="img" role="img" aria-label="Warehouse shelving stacked with cartons" style="background:linear-gradient(135deg,#9a8a70,#d9cdb8 50%,#c46a2a)"></div>
    <h3>DISTRIBUTION</h3>
    <p>Proin porta fermentum ipsum, vel porttitor turpis venenatis luctus. Vivamus volutpat eu sapien quis tempus. Aenean feugiat viverra lorem ac sagittis.</p>
    <b>MORE</b>
  </div>
  <div class="service" style="left:212px">
    <div class="img" role="img" aria-label="Printing press rollers in motion" style="background:linear-gradient(135deg,#777,#cfcfcf 45%,#c9566a 70%,#555)"></div>
    <h3>PRINTING</h3>
    <p>Proin porta fermentum ipsum, vel porttitor turpis venenatis luctus. Vivamus volutpat eu sapien quis tempus. Aenean feugiat viverra lorem ac sagittis.</p>
    <b>MORE</b>
  </div>
  <div class="service" style="left:413px">
    <div class="img" role="img" aria-label="Cardboard parcel being handed over" style="background:linear-gradient(135deg,#2c3545,#b08658 50%,#4a2a3a)"></div>
    <h3>PACKAGING</h3>
    <p>Proin porta fermentum ipsum, vel porttitor turpis venenatis luctus. Vivamus volutpat eu sapien quis tempus. Aenean feugiat viverra lorem ac sagittis.</p>
    <b>MORE</b>
  </div>
</section>

<h2 class="abs products-title">OUR PRODUCTS</h2>
<div class="abs next"><svg width="9" height="9"><path d="M3.5 2.5l2.5 2-2.5 2" fill="none" stroke="#fff"/></svg></div>

<div class="abs card" style="left:60px"><div class="img" role="img" aria-label="Calculator, pen and coffee cup on paper" style="background:linear-gradient(135deg,#c8c8c8,#f2f2f2)"></div><p>Aliquam erat volutpat</p><svg width="9" height="8"><path d="M1 4h7M5 1l3 3-3 3" fill="none" stroke="#444" stroke-width="1.1"/></svg></div>
<div class="abs card" style="left:163px"><div class="img" role="img" aria-label="Pencil cup on a desk" style="background:linear-gradient(135deg,#e6c27a,#b88a4a)"></div><p>Aliquam erat volutpat</p><svg width="9" height="8"><path d="M1 4h7M5 1l3 3-3 3" fill="none" stroke="#444" stroke-width="1.1"/></svg></div>
<div class="abs card" style="left:266px"><div class="img" role="img" aria-label="Stationery set with scissors and notebooks" style="background:linear-gradient(135deg,#ececec,#b45a9a 60%,#ddd)"></div><p>Aliquam erat volutpat</p><svg width="9" height="8"><path d="M1 4h7M5 1l3 3-3 3" fill="none" stroke="#444" stroke-width="1.1"/></svg></div>
<div class="abs card" style="left:368px"><div class="img" role="img" aria-label="Stack of yellow sticky notes" style="background:linear-gradient(135deg,#eee,#e4e36a 55%,#ddd)"></div><p>Aliquam erat volutpat</p><svg width="9" height="8"><path d="M1 4h7M5 1l3 3-3 3" fill="none" stroke="#444" stroke-width="1.1"/></svg></div>
<div class="abs card" style="left:471px"><div class="img" role="img" aria-label="Colourful erasers stacked" style="background:linear-gradient(135deg,#eee,#e0607a 45%,#3fc4c8 70%,#eee)"></div><p>Aliquam erat volutpat</p><svg width="9" height="8"><path d="M1 4h7M5 1l3 3-3 3" fill="none" stroke="#444" stroke-width="1.1"/></svg></div>
<div class="abs card" style="left:574px"><div class="img" role="img" aria-label="Pencil case with pens and scissors" style="background:linear-gradient(135deg,#eee,#2a3560 55%,#eee)"></div><p>Aliquam erat volutpat</p><svg width="9" height="8"><path d="M1 4h7M5 1l3 3-3 3" fill="none" stroke="#444" stroke-width="1.1"/></svg></div>

<footer class="abs footer">
  <div class="abs col" style="left:64px;top:17px">
    <h4>Support</h4>
    <p style="margin-top:4px">Phone : 555 201 4480</p>
    <p>info@kelbrynwares.com</p>
    <p>Contact us</p>
    <p style="font-size:8px;color:#222">Find Locaton</p>
  </div>
  <div class="abs col" style="left:205px;top:17px;width:150px">
    <h4>About us</h4>
    <p class="about">Fusce vitae lectus sit amet mi pulvinar maxi mus. Aenean placerat, nibh vel accumsan aliquet, magna nibh accumsan nibh, ac tempus nunc ipsum ac tellus. Cras augue magna, placerat eget nulla non, congue suscip-it neque. Nam et turpis non turpis cursus</p>
  </div>
  <div class="abs col" style="left:394px;top:17px">
    <h4>Quick Links</h4>
    <ul class="links"><li>Home</li><li>Contact us</li><li>About us</li><li>Locations</li><li>Products</li><li>News</li><li>Services</li><li>Help</li></ul>
  </div>
  <div class="abs col" style="left:584px;top:17px">
    <h4>Follow us on</h4>
    <div class="social"><span style="background:#2e4a8a"></span><span style="background:#2a9ad6"></span><span style="background:#333"></span><span style="background:#5aa63c"></span></div>
  </div>
</footer>
<div class="abs divider" style="left:175px"></div>
<div class="abs divider" style="left:371px"></div>
<div class="abs divider" style="left:551px"></div>

<div class="abs bottom">
  <p class="abs" style="left:61px;top:16px">Copyright © 2015 Kelbryn Wares. All Rights Reserved.</p>
  <p class="abs" style="left:61px;top:32px">Disclaimer | Support | Terms andConditions</p>
  <div class="abs round" style="left:630px;top:19px"><svg width="14" height="14"><rect x="3.5" y="4.5" width="7" height="5" fill="none" stroke="#ddd"/><path d="M3.5 4.5l3.5 3 3.5-3" fill="none" stroke="#ddd"/></svg></div>
  <div class="abs round" style="left:650px;top:19px"><svg width="14" height="14"><path d="M7 10.5V3.5M4.5 6l2.5-2.5L9.5 6" fill="none" stroke="#bbb"/></svg></div>
</div>
</body>
</html>
```